Real Estate For Sale Signage

I'm an independent agent in Lismore NSW Australia with high standards and looking for a catching 'For Sale'sign board.
I like classy, elegant, stylish and simple best.
My colours are red, white and black.
I don't have a logo or other font designs I need to stick to. I like the concept of a house or real estate design.
Before I created this project I played around on publisher and created the PDF attached. I'm not sold on it, but I don't mind the way the name has been layed out. Originally I had a white background with black & red font.
Fancy fonts for my name would be nice, but must not be busy.
Updates

Just wanted to advise that I have updated my brief and used the tools available to help get my ideas through.

Thank you for your work and time.

Kind regards
Marella

Industry/Entity Type

Real Estate

Requirements
Must have
• For Sale
Marella Quint Real Estate (must stand out)
0400 517 382 (must stand out)
17 Tallowood Street North Lismore
www.marellaquintrealestate.com.au

```html
<!DOCTYPE html>
<html lang="en">
<head>
<meta charset="utf-8">
<title>For Sale – Marella Quint Real Estate</title>
<link rel="stylesheet" href="https://fonts.googleapis.com/css2?family=Cinzel:wght@400&family=Open+Sans:wght@700&family=Noto+Serif:wght@400;700&display=swap">
<style>
  :root {
    --sign-white: #ffffff;
    --ink-black: #111111;
    --band-black: #050505;
    --band-grey: #8a8a8a;
    --brand-red: #e30613;
    --title-red: #c8000a;
    --deep-red: #9c0008;
    --frame-grey: #9a9a9a;
  }
  html, body {
    margin: 0;
    padding: 0;
    width: 957px;
    height: 1200px;
    overflow: hidden;
    background: var(--sign-white);
  }
  .sign-board {
    display: block;
    width: 957px;
    height: 1200px;
  }
  .headline {
    font-family: "Open Sans", Arial, sans-serif;
    font-weight: 700;
    font-size: 172px;
    fill: var(--sign-white);
    stroke: var(--brand-red);
    stroke-width: 6px;
    paint-order: stroke;
    letter-spacing: 3px;
  }
  .agency-name {
    font-family: "Cinzel", "Times New Roman", serif;
    font-weight: 400;
    font-size: 98px;
    fill: var(--ink-black);
  }
  .agency-tagline {
    font-family: "Noto Serif", "Times New Roman", serif;
    font-weight: 400;
    font-size: 70px;
    fill: var(--title-red);
  }
  .phone-number {
    font-family: "Noto Serif", Georgia, serif;
    font-weight: 700;
    font-size: 100px;
    fill: var(--sign-white);
  }
  .street-address {
    font-family: "Noto Serif", Georgia, serif;
    font-weight: 700;
    font-size: 36px;
    fill: var(--sign-white);
  }
  .web-address {
    font-family: "Noto Serif", Georgia, serif;
    font-weight: 400;
    font-size: 30px;
    fill: var(--sign-white);
  }
</style>
</head>
<body>
<svg class="sign-board" viewBox="0 0 957 1200" xmlns="http://www.w3.org/2000/svg" aria-label="For Sale sign for Marella Quint Real Estate">
  <defs>
    <radialGradient id="headerSheen" cx="0.82" cy="0.1" r="0.6">
      <stop offset="0" stop-color="var(--band-grey)"/>
      <stop offset="1" stop-color="var(--band-black)"/>
    </radialGradient>
    <linearGradient id="footerRed" x1="0" y1="0" x2="0" y2="1">
      <stop offset="0" stop-color="#ff1a1a"/>
      <stop offset="1" stop-color="#c8000a"/>
    </linearGradient>
  </defs>

  <rect class="board-frame" x="14" y="10" width="922" height="1175" fill="var(--sign-white)" stroke="var(--frame-grey)" stroke-width="2"/>

  <path class="header-accent" d="M0 0 H922 V215 C700 260 300 280 0 460 Z" fill="var(--brand-red)"/>
  <path class="header-band" d="M0 0 H922 V200 C700 240 300 250 0 410 Z" fill="url(#headerSheen)"/>
  <text class="headline" x="468" y="182" text-anchor="middle">For Sale</text>

  <circle class="brand-dot" cx="451" cy="460" r="150" fill="var(--brand-red)"/>

  <text class="agency-name" x="470" y="735" text-anchor="middle">Marella Quint</text>
  <text class="agency-tagline" x="462" y="835" text-anchor="middle">Real Estate</text>

  <path class="footer-accent" d="M0 905 C400 870 760 860 922 745 V1165 H0 Z" fill="var(--deep-red)"/>
  <path class="footer-band" d="M0 925 C420 895 780 880 922 775 V1165 H0 Z" fill="url(#footerRed)"/>
  <text class="phone-number" x="462" y="1030" text-anchor="middle">Tel.0400 517 382</text>
  <text class="street-address" x="462" y="1092" text-anchor="middle">17 Tallowood Street North Lismore</text>
  <text class="web-address" x="462" y="1142" text-anchor="middle">www.marellaquintrealestate.com.au</text>
</svg>
</body>
</html>
```